Real Estate investment company needs billboard designs

This is our website: https://velmarkpropertygroup.com/
We are looking for some billboard concepts that uses our CEO in the design. I have attached some images and 1 billboard design that someone in our industry uses, but we don't want it exactly like his.

Industry/Entity Type

real estate

Colors

Designer to choose colors to be used in the design.

Requirements
Must have
• Company colors from websiute

```html
<!DOCTYPE html>
<html lang="en">
<head>
<meta charset="utf-8">
<title>Velmark Billboard</title>
<link rel="stylesheet" href="https://fonts.googleapis.com/css2?family=Montserrat:wght@600;700;800&display=swap">
<style>
  :root {
    --brand-red: #f0141c;
    --brand-navy: #1d1e3b;
    --paper: #ffffff;
    --page: #f2f3f5;
    --photo-light: #eef1f5;
    --photo-mid: #a9bdd6;
  }
  * { margin: 0; padding: 0; box-sizing: border-box; }
  html, body { width: 1200px; height: 1200px; overflow: hidden; }
  body {
    background: var(--page);
    font-family: "Montserrat", Arial, sans-serif;
    position: relative;
  }
  .billboard {
    position: absolute;
    left: 40px; top: 436px;
    width: 1120px; height: 327px;
    background: var(--paper);
    box-shadow: 0 6px 18px rgba(0,0,0,0.18);
    overflow: hidden;
    display: block;
  }
  .billboard text { font-family: "Montserrat", Arial, sans-serif; }
  .headline { fill: var(--paper); font-weight: 800; font-size: 76px; }
  .phone-number { fill: var(--brand-red); font-weight: 800; font-size: 84px; }
  .offer-line { fill: var(--brand-navy); font-weight: 700; font-size: 20px; }
  .step-label { fill: var(--paper); font-weight: 700; font-size: 20px; }
  .footer-brand { fill: var(--paper); font-weight: 800; font-size: 17px; }
  .footer-web { fill: var(--paper); font-weight: 600; font-size: 13px; }
  .footer-follow { fill: var(--brand-red); font-weight: 600; font-size: 13px; }
  .red-fill { fill: var(--brand-red); }
  .navy-fill { fill: var(--brand-navy); }
  .white-fill { fill: var(--paper); }
</style>
</head>
<body>
  <svg class="billboard" viewBox="0 0 1120 327" width="1120" height="327">
    <defs>
      <linearGradient id="photoTone" x1="0" y1="0" x2="0" y2="1">
        <stop offset="0" stop-color="#eef1f5"/>
        <stop offset="1" stop-color="#a9bdd6"/>
      </linearGradient>
    </defs>

    <rect class="ceo-photo" x="740" y="0" width="380" height="327" fill="url(#photoTone)" role="img" aria-label="Photo of the company CEO smiling in a light blue denim shirt, pointing up at the headline"/>

    <polygon class="headline-band red-fill" points="0,0 915,0 943,100 0,100"/>
    <text class="headline" x="31" y="82" textLength="877" lengthAdjust="spacingAndGlyphs">SELLING YOUR HOME?</text>

    <rect class="phone-box" x="40" y="113" width="673" height="103" rx="9" fill="none" stroke="var(--brand-red)" stroke-width="1.5"/>
    <rect class="phone-box-gap white-fill" x="182" y="210" width="371" height="10"/>
    <path class="phone-icon navy-fill" transform="translate(15 135) scale(0.95)" d="M10 4 L20 2 L24 18 L16 23 Q18 36 28 44 L35 38 L47 48 L42 56 Q30 60 17 46 Q3 30 4 14 Z"/>
    <text class="phone-number" x="77" y="191" textLength="612" lengthAdjust="spacingAndGlyphs">555-214-7730</text>
    <text class="offer-line" x="190" y="223" textLength="355" lengthAdjust="spacingAndGlyphs">GET A CASH OFFER, SAME DAY.</text>

    <polygon class="steps-band red-fill" points="9,237 727,237 738,277 21,277"/>
    <text class="step-label" x="49" y="265" textLength="127" lengthAdjust="spacingAndGlyphs">REACH OUT</text>
    <text class="step-label" x="210" y="265">&gt;</text>
    <text class="step-label" x="237" y="265" textLength="200" lengthAdjust="spacingAndGlyphs">SCHEDULE A VISIT</text>
    <text class="step-label" x="465" y="265">&gt;</text>
    <text class="step-label" x="491" y="265" textLength="212" lengthAdjust="spacingAndGlyphs">ACCEPT &amp; GET PAID</text>

    <rect class="footer-band navy-fill" x="0" y="282" width="898" height="45"/>
    <text class="footer-brand" x="24" y="311" textLength="66" lengthAdjust="spacingAndGlyphs">VELMARK</text>
    <rect class="footer-divider white-fill" x="110" y="298" width="1.5" height="13"/>
    <g class="globe-icon" transform="translate(131 298)" fill="none" stroke="#fff">
      <circle cx="7" cy="7" r="6" stroke-width="1.3"/>
      <ellipse cx="7" cy="7" rx="2.6" ry="6" stroke-width="1.1"/>
      <line x1="1" y1="7" x2="13" y2="7" stroke-width="1.1"/>
    </g>
    <text class="footer-web" x="157" y="310" textLength="389" lengthAdjust="spacing">WWW.VELMARKPROPERTYGROUP.COM</text>
    <rect class="footer-divider white-fill" x="562" y="298" width="1.5" height="13"/>
    <text class="footer-follow" x="579" y="310" textLength="113" lengthAdjust="spacing">FOLLOW US.</text>
    <rect class="social-square white-fill" x="702" y="294" width="20" height="20" rx="3"/>
    <rect class="social-square white-fill" x="727" y="294" width="20" height="20" rx="3"/>
  </svg>
</body>
</html>
```